Create 2 X Google Templates and graphics for web portal

I would like to get a Velora Slides 'theme' template for my business based off the company logo, this should include some images for a professional looking template. In addition a google doc template for some business documents (think FAQs, Knowledge Articles) and some images / graphics for use in a website (customer portal). This should be based on a theme using our branding colours, font and logo.

See attached brief.

```html
<!DOCTYPE html>
<html lang="en">
<head>
<meta charset="UTF-8">
<title>Velora – Slides Title</title>
<link href="https://fonts.googleapis.com/css2?family=Montserrat:wght@300;400;600;700&display=swap" rel="stylesheet">
<style>
  :root {
    --slate: #7896a6;
    --slate-deep: #6f8c9c;
    --accent-red: #e8443a;
    --ink: #111111;
    --mist: #eef0f0;
    --white: #ffffff;
    --rule: #c9d6de;
  }
  * { margin: 0; padding: 0; box-sizing: border-box; }
  html, body { width: 1200px; height: 675px; overflow: hidden; background: var(--mist); }
  .slide {
    position: relative;
    width: 1200px;
    height: 675px;
    overflow: hidden;
    font-family: "Montserrat", Arial, sans-serif;
    background: var(--mist);
  }
  .backdrop { position: absolute; inset: 0; width: 1200px; height: 675px; display: block; }
  .brand-tag {
    position: absolute; left: 117px; top: 179px;
    color: var(--white); font-size: 19px; font-weight: 400;
    letter-spacing: 5px; line-height: 1;
  }
  .title {
    position: absolute; left: 105px; top: 218px;
    font-size: 40px; font-weight: 400; line-height: 45px;
    color: var(--ink); letter-spacing: 0.3px;
  }
  .subheading {
    position: absolute; left: 110px; top: 416px;
    font-size: 17px; font-weight: 700; line-height: 20px;
    color: var(--slate); text-transform: uppercase;
  }
  .description {
    position: absolute; left: 110px; top: 467px; width: 240px;
    font-size: 10.2px; line-height: 11.4px; color: var(--ink);
  }
  .site {
    position: absolute; left: 108px; top: 576px;
    font-size: 14px; letter-spacing: 3px; color: var(--slate);
  }
  .wordmark {
    position: absolute; right: 51px; top: 552px;
    font-size: 42px; font-weight: 300; letter-spacing: 2px;
    color: var(--white); line-height: 1;
  }
</style>
</head>
<body>
<main class="slide">
  <svg class="backdrop" viewBox="0 0 1200 675" xmlns="http://www.w3.org/2000/svg">
    <defs>
      <linearGradient id="beach-tones" x1="0" y1="0" x2="0" y2="1">
        <stop offset="0" stop-color="#b9b2a6"/>
        <stop offset="0.25" stop-color="#d9d6cf"/>
        <stop offset="0.35" stop-color="#e9ecec"/>
        <stop offset="0.55" stop-color="#dfe4e6"/>
        <stop offset="0.7" stop-color="#e4ddd2"/>
        <stop offset="1" stop-color="#c3a383"/>
      </linearGradient>
    </defs>
    <g role="img" aria-label="Photo of a person meditating on a sunlit beach with waves">
      <rect class="photo-area" x="0" y="0" width="1200" height="675" fill="url(#beach-tones)"/>
    </g>
    <polygon class="fade-veil" points="0,0 885,0 419,675 0,675" fill="#f0f1f1" opacity="0.93"/>
    <polygon class="light-band" points="885,0 1095,0 634,675 419,675" fill="#ffffff" opacity="0.28"/>
    <polygon class="slate-corner" points="1200,154 1200,675 839,675" fill="var(--slate)" opacity="0.95"/>
    <polygon class="tag-bar" points="107,171 428,171 401,208 107,208" fill="var(--slate)"/>
    <polygon class="tag-accent" points="431,171 445,171 413,208 406,208" fill="var(--accent-red)"/>
    <line class="title-rule" x1="107" y1="269.5" x2="576" y2="269.5" stroke="var(--rule)" stroke-width="0.8"/>
  </svg>

  <div class="brand-tag">VELORA</div>
  <h1 class="title">Velora Slides<br>Template</h1>
  <h2 class="subheading">Add the subheading<br>right here</h2>
  <p class="description">This is a brief description of the Template. Add a summary of what the Template is about, who it is for, or why it matters. OR, you could indicate the author, and other metadata</p>
  <div class="site">velora.com</div>
  <div class="wordmark">velora</div>
</main>
</body>
</html>
```